Real Estate Sign 24" wide X 36" long

We are looking for creative modern design for a real estate sign, Wow us but remember its about people driving by the sign and retaining our brand.

The Brisket Hollow Logo need to be at the bottom of sign. Please use change colors to fit your design.

Also need the following on the sign:

555.380.4162
Lev Marchetti Piers Okafor
Marchetti & Okafor Logo
Lev and Piers's picture

Our current sign we are replacing is attached: "Pemberly M&O". We are replacing for more modern beautiful design that is one piece.

A rough draft is also attached...but be creative...don't think inside a box.

Target Market(s)

Home Buyers and Sellers

Industry/Entity Type

Real Estate Agent

Colors

Designer to choose colors to be used in the design.

Requirements
Must have
• The sign must be 24" wide X 36" tall. This will be the sign we hang in front of homes for sale.
Nice to have
• Background design that works well would be nice.
• Our business is in Florida...would be nice to have background palm trees, sun, beach...but not necessary.

```html
<!DOCTYPE html>
<html lang="en">
<head>
<meta charset="utf-8">
<title>Marchetti &amp; Okafor Realty Signs</title>
<link href="https://fonts.googleapis.com/css2?family=Lato:wght@300;400&family=Crimson+Text:wght@700&family=Cinzel:wght@600&display=swap" rel="stylesheet">
<style>
  :root {
    --backdrop: #e9ebee;
    --paper: #ffffff;
    --teal: #2a93a4;
    --navy: #13203f;
    --navy-mid: #163a64;
    --navy-bar: #10284c;
    --banner: #2a3a5c;
  }
  * { margin: 0; padding: 0; box-sizing: border-box; }
  html, body { width: 1200px; height: 1087px; overflow: hidden; background: var(--backdrop); }
  body { position: relative; font-family: "Lato", sans-serif; }

  .sign { position: absolute; background: var(--paper); overflow: hidden; box-shadow: 0 6px 18px rgba(0,0,0,.18); }

  .brand { position: absolute; left: 0; right: 0; display: flex; align-items: center; justify-content: center; gap: 10px; line-height: 1; }
  .brand-square { width: 14px; height: 14px; background: var(--teal); }
  .brand-name { font-family: "Lato", sans-serif; font-weight: 300; color: var(--teal); white-space: nowrap; }

  .phone { position: absolute; left: 0; right: 0; text-align: center; font-family: "Crimson Text", serif; font-weight: 700; color: var(--navy); line-height: 1; white-space: nowrap; }
  .website { position: absolute; left: 0; right: 0; text-align: center; font-family: "Lato", sans-serif; font-weight: 400; color: var(--teal); line-height: 1; white-space: nowrap; }

  /* Yard sign (portrait) */
  .yard-sign { left: 145px; top: 224px; width: 433px; height: 648px; }
  .yard-sign .brand { top: 118px; }
  .yard-sign .brand-name { font-size: 34px; }
  .yard-sign .phone { top: 188px; font-size: 72px; letter-spacing: 1px; }
  .yard-sign .website { top: 266px; font-size: 22px; }
  .yard-art { position: absolute; left: 0; top: 0; width: 433px; height: 648px; }

  .portrait { position: absolute; border-radius: 70px 70px 0 0; }
  .portrait-lev { left: 168px; top: 402px; width: 140px; height: 202px;
    background: linear-gradient(180deg, #5a6f86 0%, #2a3a52 55%, #1b2638 100%); }
  .portrait-piers { left: 292px; top: 388px; width: 141px; height: 216px;
    background: linear-gradient(180deg, #6a7c92 0%, #2c3c55 55%, #1c2739 100%); }

  .name-bar { position: absolute; left: 0; right: 0; top: 604px; height: 44px; display: flex; align-items: center; font-family: "Lato", sans-serif; font-weight: 300; color: #fff; font-size: 15px; }
  .name-bar .broker { width: 153px; text-align: center; font-size: 13px; }
  .name-bar .agent { position: absolute; width: 140px; text-align: center; }
  .name-bar .agent-lev { left: 151px; }
  .name-bar .agent-piers { left: 289px; }

  /* Open house sign (landscape) */
  .open-house-sign { left: 690px; top: 400px; width: 432px; height: 327px;
    background: linear-gradient(180deg, #f6f9fb 0%, #eef3f6 100%); }
  .open-house-sign .brand { top: 101px; }
  .open-house-sign .brand-name { font-size: 34px; }
  .open-house-arrow { position: absolute; left: 13px; top: 158px; width: 402px; height: 82px; }
  .open-house-label { position: absolute; left: 13px; top: 171px; width: 396px; height: 54px; display: flex; align-items: center; justify-content: center; font-family: "Cinzel", serif; font-weight: 600; color: #fff; font-size: 39px; letter-spacing: 1px; }
  .open-house-sign .phone { top: 238px; font-size: 56px; }
  .open-house-sign .website { top: 298px; font-size: 18px; }
</style>
</head>
<body>

<section class="sign yard-sign">
  <div class="brand"><span class="brand-square"></span><span class="brand-name">Marchetti &amp; Okafor</span></div>
  <div class="phone">555.380.4162</div>
  <div class="website">MarchettiOkaforRealty.com</div>

  <svg class="yard-art" viewBox="0 0 433 648" role="img" aria-label="Navy backdrop with faint palm tree silhouettes">
    <defs>
      <linearGradient id="backdropFill" x1="0" y1="0" x2="1" y2="1">
        <stop offset="0" stop-color="#163a64"/>
        <stop offset="0.6" stop-color="#1b3f68"/>
        <stop offset="1" stop-color="#132f55"/>
      </linearGradient>
    </defs>
    <path d="M0 420 Q200 330 433 338 L433 346 Q220 352 0 470 Z" fill="var(--teal)"/>
    <path d="M0 492 Q230 370 433 352 L433 648 L0 648 Z" fill="url(#backdropFill)"/>
    <rect x="0" y="604" width="433" height="44" fill="var(--navy-bar)"/>
    <rect x="0" y="604" width="153" height="44" fill="#1a3a66"/>
  </svg>

  <div class="portrait portrait-lev" role="img" aria-label="Photo of Lev Marchetti"></div>
  <div class="portrait portrait-piers" role="img" aria-label="Photo of Piers Okafor"></div>

  <div class="name-bar">
    <span class="broker">Brisket Hollow</span>
    <span class="agent agent-lev">Lev Marchetti</span>
    <span class="agent agent-piers">Piers Okafor</span>
  </div>
</section>

<section class="sign open-house-sign">
  <div class="brand"><span class="brand-square"></span><span class="brand-name">Marchetti &amp; Okafor</span></div>
  <svg class="open-house-arrow" viewBox="0 0 402 82" aria-hidden="true">
    <path d="M0 13 L340 13 L340 0 L402 41 L340 82 L340 67 L0 67 L18 40 Z" fill="var(--banner)"/>
  </svg>
  <div class="open-house-label">OPEN HOUSE</div>
  <div class="phone">555.380.4162</div>
  <div class="website">MarchettiOkaforRealty.com</div>
</section>

</body>
</html>
```